Twirly Puff Cotton Candy

Looking for a logo design and business cards to help a 13 year old entrepreneur promote her cotton candy business.
Contact Information for Business Card
Name, Phone & Email
Colors
E54698
E96AAD
F1A4CE
F9D9EA
FCEFF6
A7469A
B969AE
D3A5CF
EDDBEB
F8F0F9
6B429C
8869AF
B7A5CE
E3DAEB
F3F0F8
Requirements
Must have
- A fun feel that is appropriate for a teenage girl selling cotton candy

```html
<!DOCTYPE html>
<html lang="en">
<head>
<meta charset="utf-8">
<title>Twirly Puff Cotton Candy – Business Cards</title>
<link href="https://fonts.googleapis.com/css2?family=Amatic+SC:wght@700&family=Mulish:wght@700&display=swap" rel="stylesheet">
<style>
  :root {
    --bg: #ab9888;
    --card-white: #ffffff;
    --card-pink: #efa8cd;
    --pink-strong: #e54698;
    --pink-mid: #e96aad;
    --pink-pale: #f9d9ea;
    --purple: #6b429c;
  }
  * { margin: 0; padding: 0; box-sizing: border-box; }
  html, body { width: 1200px; height: 1200px; overflow: hidden; }
  body { background: var(--bg); position: relative; }

  .card {
    position: absolute;
    top: 480px;
    width: 419px;
    height: 240px;
    border-radius: 19px;
    overflow: hidden;
  }
  .card--front { left: 156px; background: var(--card-white); }
  .card--back  { left: 624px; background: var(--card-pink); }

  .brand {
    position: absolute;
    display: flex;
    align-items: center;
    gap: 8px;
    font-family: 'Amatic SC', cursive;
    font-weight: 700;
    color: var(--pink-strong);
    line-height: 0.9;
  }
  .brand__dot {
    width: 30px; height: 30px;
    border-radius: 50%;
    background: var(--pink-pale);
    flex: none;
  }
  .brand__name { display: flex; flex-direction: column; }
  .brand__title { font-size: 38px; letter-spacing: 0.5px; }
  .brand__tag { font-size: 17px; letter-spacing: 2px; }

  .card--front .brand { left: 50%; transform: translateX(-50%); top: 26px; }
  .card--back .brand { left: 16px; bottom: 18px; }
  .card--back .brand__title { font-size: 46px; }
  .card--back .brand__tag { font-size: 20px; }
  .card--back .brand__dot { width: 38px; height: 38px; background: var(--pink-pale); }

  .holder {
    position: absolute;
    top: 132px; left: 0; right: 0;
    text-align: center;
    font-family: 'Amatic SC', cursive;
    font-weight: 700;
    font-size: 30px;
    letter-spacing: 1px;
    color: var(--pink-strong);
  }
  .divider {
    position: absolute;
    top: 177px;
    height: 1.5px;
    width: 153px;
    background: var(--pink-strong);
  }
  .divider--left { left: 20px; }
  .divider--right { left: 246px; }
  .contact-icons {
    position: absolute;
    top: 169px; left: 186px;
    display: flex; gap: 12px;
  }
  .contact-icons svg { width: 17px; height: 17px; fill: var(--purple); }
  .contact-lines {
    position: absolute;
    top: 193px; left: 0; right: 0;
    text-align: center;
    font-family: 'Mulish', sans-serif;
    font-weight: 700;
    font-size: 11.5px;
    line-height: 15px;
    color: var(--purple);
  }
</style>
</head>
<body>
  <section class="card card--front">
    <div class="brand">
      <div class="brand__name">
        <span class="brand__title">TWIRLY PUFF</span>
        <span class="brand__tag">COTTON CANDY</span>
      </div>
      <span class="brand__dot"></span>
    </div>
    <p class="holder">MIA CARTER</p>
    <span class="divider divider--left"></span>
    <div class="contact-icons">
      <svg viewBox="0 0 24 24" aria-label="Phone"><path d="M6.6 10.8a15.1 15.1 0 0 0 6.6 6.6l2.2-2.2a1 1 0 0 1 1-.25 11.4 11.4 0 0 0 3.6.57 1 1 0 0 1 1 1V20a1 1 0 0 1-1 1A17 17 0 0 1 3 4a1 1 0 0 1 1-1h3.5a1 1 0 0 1 1 1c0 1.25.2 2.45.57 3.57a1 1 0 0 1-.25 1z"/></svg>
      <svg viewBox="0 0 24 24" aria-label="Email"><path d="M2 5h20v14H2z M3.5 6.5 12 13l8.5-6.5" fill="none" stroke="#6b429c" stroke-width="0"/><path d="M2 5h20v14H2zm2 2v.4l8 5.6 8-5.6V7zm0 2.8V17h16V9.8l-8 5.6z"/></svg>
    </div>
    <span class="divider divider--right"></span>
    <div class="contact-lines">
      <p>07. 4821. 3390</p>
      <p>mia@twirlypuff.com</p>
    </div>
  </section>

  <section class="card card--back">
    <div class="brand">
      <div class="brand__name">
        <span class="brand__title">TWIRLY PUFF</span>
        <span class="brand__tag">COTTON CANDY</span>
      </div>
      <span class="brand__dot"></span>
    </div>
  </section>
</body>
</html>
```